World first health care product in tablet form to help save relationships and marriages

The product known as Venquara is in tablet form 470mg and has 30 to a packet the packet size is approx 11cm in length x 4cm We want to use the color of the image attached for the package and cornflower blue for our name Venquara. We also need to mention close to our name....... maintaining relationships with increased libido and desire ...... Our tablets are in a tamper-proof blister pack inserted into the package. We do not have a logo as yet, we are thinking of ven in small white letters and then QUARA in large letters in cornflower blue or something a bit darker. (The O could also contain a smiley face) We are not that fussed with a logo as yet, maybe down the track if our product works and sells. As of today business in Australia has ground to a halt with this coronavirus and its as bad as you could imagine. Please help us make this new product work with a fabulous packet design.
Target Market(s)
females and males
Industry/Entity Type
Pharmaceutical
Requirements
Must have
- the colors of the images attached and cornflower blue

```html
<!DOCTYPE html>
<html lang="en">
<head>
<meta charset="utf-8">
<title>Venquara – pack front</title>
<link rel="stylesheet" href="https://fonts.googleapis.com/css2?family=Barlow+Semi+Condensed:wght@700&family=Lato:wght@400;900&family=Poppins:wght@700&display=swap">
<style>
  :root {
    --stage: #3a3a3c;
    --pack-blue: #2aa7da;
    --pack-blue-deep: #2295c8;
    --pack-blue-light: #35b0e2;
    --name-blue: #16679c;
    --white: #ffffff;
  }
  * { margin: 0; padding: 0; box-sizing: border-box; }
  html, body {
    width: 1200px; height: 568px; overflow: hidden;
    background: var(--stage);
  }
  .canvas { position: relative; width: 1200px; height: 568px; }
  .pack-front {
    position: absolute; left: 102px; top: 102px;
    width: 997px; height: 364px;
    background: var(--pack-blue);
    overflow: hidden;
  }
  .pack-texture {
    position: absolute; inset: 0;
    background: linear-gradient(150deg, var(--pack-blue-light) 0%, var(--pack-blue) 35%, var(--pack-blue-deep) 60%, var(--pack-blue) 100%);
  }
  .dose-info {
    position: absolute; right: 26px; top: 42px;
    font-family: "Barlow Semi Condensed", sans-serif;
    font-weight: 700; font-size: 23px; letter-spacing: 0.5px;
    color: var(--white); line-height: 1;
    padding-bottom: 6px;
    border-bottom: 3px solid var(--white);
  }
  .pack-type { position: absolute; left: 0; top: 0; }
  .brand-prefix {
    font-family: "Lato", sans-serif; font-weight: 900;
    font-size: 84px; fill: var(--white);
  }
  .brand-rule { fill: var(--white); }
  .tagline {
    font-family: "Lato", sans-serif; font-weight: 400;
    font-size: 23px; fill: var(--white);
  }
  .brand-name {
    font-family: "Poppins", sans-serif; font-weight: 700;
    font-size: 272px; fill: var(--name-blue);
  }
</style>
</head>
<body>
  <main class="canvas">
    <section class="pack-front">
      <div class="pack-texture" role="img" aria-label="Faceted geometric pattern in layered blue tones"></div>

      <p class="dose-info">470MG | 30 SOFT CAPSULES</p>

      <svg class="pack-type" width="997" height="364" viewBox="0 0 997 364">
        <text class="brand-prefix" x="295" y="208" text-anchor="end">ven</text>
        <rect class="brand-rule" x="129" y="231" width="166" height="2"></rect>
        <text class="tagline" text-anchor="end">
          <tspan x="295" y="259">maintaining</tspan>
          <tspan x="295" y="288">relationships</tspan>
          <tspan x="295" y="317">with increased</tspan>
          <tspan x="295" y="346">libido and desire</tspan>
        </text>
        <text class="brand-name" x="315" y="336" textLength="673" lengthAdjust="spacingAndGlyphs">QUARA</text>
      </svg>
    </section>
  </main>
</body>
</html>
```